Software Specialist in Artificial Intelligence innovation needs a smart and professional looking bus

Prefers a clean and professional design, yet portraying a class of its own and a world-class feel. We develop state-of-the-art software automation engines by deploying artificial intelligence that simulates the smartest brains that are able to simulate a human consultant and/or data scientist. Both single-sided or double-sided design is acceptable. Do not refer too much to our current website as we are also in the process of revamping it so that it better reflects who we are and what we do.
Updates

Project Deadline Extended
Reason: A substantial number of designs submitted to date deviates a fair bit from requirements and expectations. Feedbacks will be provided to all parties by today and as such, an extension is catered to accomodate re-submissions.

Target Market(s)

Software technology companies, software developers, enterprise clients that requires automation supported by Artificial Intelligence driven software solutions.

Industry/Entity Type

Software

Contact Information for Business Card

Marcus Tan
Chief Innovator
marcustan@veltrixia.com
mobile: +65 94567312
Company Name: Veltrixia Pte Ltd
Address: 14 Sorbank Road #05-11 Harlowe Point, Singapore 538422
Telephone: +65 63417250
Website: www.Veltrixia.com
Please do not include the titles of the above fields.

Font styles to use
Sans Serif
Other font styles liked:
• Calibri, Futura Condensed

Requirements
Must have
• Portrays a professional and innovative image. Should reflect that the company is into Artificial Intelligence software development, high tech kind of feel.
Nice to have
• A plus point would be if you can even come up with a new company logo for us, representing who we are. Our current company logo is attached.
Should not have
• Fanciful stuffs as it must portray a professional image. Prefers not to have the cloud "image" as part of the logo or in the name card.

```html
<!DOCTYPE html>
<html lang="en">
<head>
<meta charset="utf-8">
<title>Veltrixia Business Card</title>
<link rel="stylesheet" href="https://fonts.googleapis.com/css2?family=Open+Sans:wght@700&family=Share+Tech+Mono&display=swap">
<style>
  :root {
    --backdrop: #d9d6cf;
    --card: #0b0b0c;
    --card-edge: #1a1a1c;
    --ink: #f4f4f4;
    --ink-soft: #e2e2e2;
    --accent: #2f8fd8;
    --circuit: rgba(120, 130, 140, 0.14);
  }
  * { margin: 0; padding: 0; box-sizing: border-box; }
  html, body {
    width: 1200px;
    height: 800px;
    overflow: hidden;
    background: var(--backdrop);
  }
  .stage {
    width: 1200px;
    height: 800px;
    display: flex;
    align-items: center;
    justify-content: center;
    gap: 60px;
  }
  .card {
    position: relative;
    width: 520px;
    height: 297px;
    background: var(--card);
    border: 1px solid var(--card-edge);
    box-shadow: 0 10px 28px rgba(0, 0, 0, 0.35);
    overflow: hidden;
  }
  .circuit-texture {
    position: absolute;
    background: linear-gradient(135deg, transparent, var(--circuit) 45%, transparent);
  }
  .card-front .circuit-left { left: 0; top: 120px; width: 170px; height: 177px; }
  .card-front .circuit-right { right: 0; top: 0; width: 230px; height: 297px; }
  .card-back .circuit-top { right: 0; top: 0; width: 260px; height: 150px; }

  .brand {
    position: absolute;
    left: 0; right: 0; top: 98px;
    display: flex;
    flex-direction: column;
    align-items: center;
  }
  .brand-lockup {
    display: flex;
    align-items: center;
    gap: 14px;
  }
  .brand-dot {
    width: 38px;
    height: 38px;
    border-radius: 50%;
    background: var(--accent);
  }
  .brand-name {
    font-family: "Open Sans", sans-serif;
    font-weight: 700;
    font-size: 50px;
    line-height: 1;
    color: var(--ink);
    letter-spacing: -0.5px;
  }
  .brand-tagline {
    margin-top: 10px;
    font-family: "Open Sans", sans-serif;
    font-weight: 700;
    font-size: 16px;
    color: var(--ink);
    white-space: nowrap;
  }

  .contact {
    position: absolute;
    left: 40px;
    top: 34px;
    font-family: "Share Tech Mono", monospace;
    color: var(--ink-soft);
    font-size: 17px;
    line-height: 1.3;
    white-space: nowrap;
  }
  .contact-name {
    padding-left: 150px;
    font-size: 24px;
    color: var(--ink);
  }
  .contact-title {
    padding-left: 110px;
    margin-bottom: 12px;
  }
  .contact-address { margin-bottom: 14px; }
  .contact-address .indent { display: block; padding-left: 40px; }
  .contact-address .indent-more { display: block; padding-left: 52px; }
  .contact-lines span { display: block; }
  .contact-lines .phone { padding-left: 60px; }
</style>
</head>
<body>
  <main class="stage">
    <section class="card card-front">
      <div class="circuit-texture circuit-left" role="img" aria-label="Faint circuit-board line pattern"></div>
      <div class="circuit-texture circuit-right" role="img" aria-label="Faint circuit-board line pattern"></div>
      <div class="brand">
        <div class="brand-lockup">
          <span class="brand-dot"></span>
          <span class="brand-name">Veltrixia</span>
        </div>
        <p class="brand-tagline">Building the next Intelligent Enterprise</p>
      </div>
    </section>

    <section class="card card-back">
      <div class="circuit-texture circuit-top" role="img" aria-label="Faint circuit-board line pattern"></div>
      <div class="contact">
        <p class="contact-name">Marcus Tan</p>
        <p class="contact-title">Chief Innovator</p>
        <p class="contact-address">Address: 14 Sorbank Road
          <span class="indent">05-11 Harlowe Point,</span>
          <span class="indent-more">Singapore 538422</span>
        </p>
        <p class="contact-lines">
          <span class="phone">+65 94567312</span>
          <span>marcustan@veltrixia.com</span>
          <span class="phone">www.Veltrixia.com</span>
        </p>
      </div>
    </section>
  </main>
</body>
</html>
```